Detail Shop Business card design

i need a business card design for my new detailing company called 'Brenner's Detail Shop'. i want an all black and white design . simple, direct and to the point. i want the designer to choose a fitting font to match the logothe front should have logo, address, phone and email and the back side should have a slogan and text indicating that we offer services on anything including cars, trucks, motorcycles and RVs. slogan will read "we take pride in your ride"
maybe also very small on the back side the IG icon with Brenners_Detail_Shop

phone 482.615.7734
address 7384 E Harlow Ave
Spokane WA 99342
email: BrennersDetail@quorvail.com

Target Market(s)

all ages , auto enthusiasts

Industry/Entity Type

Automotive

Contact Information for Business Card

the front should have logo, address, phone and email and the back side should have a slogan and text indicating that we offer services on anything including cars, trucks, motorcycles and RVs. slogan will read "we take pride in your ride"

phone 482.615.7734
address 7384 E Harlow Ave
Spokane WA 99342

Colors
000000
ffffff

Requirements
Must have
• bold font and very simple design with good spacing
Nice to have
• anything creative from the designer indicating we service any types of vehicles
Should not have
• any colors ,

```html
<!DOCTYPE html>
<html lang="en">
<head>
<meta charset="utf-8">
<title>Brenner's Detail Shop – Business Card</title>
<link href="https://fonts.googleapis.com/css2?family=Roboto+Slab:wght@400;700&display=swap" rel="stylesheet">
<style>
  :root {
    --ink: #000000;
    --paper: #ffffff;
    --backdrop: #232323;
    --rule: #555555;
  }
  * { box-sizing: border-box; margin: 0; padding: 0; }
  html, body { width: 1200px; height: 930px; overflow: hidden; }
  body {
    background: var(--backdrop);
    font-family: "Roboto Slab", Georgia, serif;
    color: var(--ink);
    position: relative;
  }
  .card {
    position: absolute;
    width: 700px;
    height: 400px;
    background: var(--paper);
    border-radius: 16px;
    overflow: hidden;
  }
  .card--back { left: 110px; top: 43px; }
  .card--front { left: 390px; top: 487px; }

  .brand {
    display: flex;
    align-items: center;
    gap: 12px;
    font-weight: 700;
    color: var(--ink);
    white-space: nowrap;
  }
  .brand__dot {
    width: 30px; height: 30px;
    border-radius: 50%;
    background: var(--ink);
    flex: none;
  }

  /* back side */
  .card--back .brand {
    position: absolute;
    left: 0; right: 0; top: 100px;
    justify-content: center;
    font-size: 32px;
  }
  .slogan {
    position: absolute;
    left: 140px; right: 140px; top: 232px;
    display: flex; align-items: center; gap: 14px;
    font-size: 16px; letter-spacing: 1px;
    text-transform: uppercase;
    white-space: nowrap;
  }
  .slogan::before, .slogan::after {
    content: ""; flex: 1; height: 1px; background: var(--ink);
  }
  .services {
    position: absolute;
    left: 140px; right: 140px; top: 266px;
    text-align: center;
    font-size: 18px; letter-spacing: 1px;
    text-transform: uppercase;
    padding-top: 12px;
    border-top: 1px solid var(--ink);
  }

  /* front side */
  .card--front .brand {
    position: absolute;
    right: 40px; top: 70px;
    font-size: 28px;
  }
  .front__rule {
    position: absolute;
    left: 40px; right: 40px; top: 180px;
    height: 1px; background: var(--rule);
  }
  .address {
    position: absolute;
    right: 40px; top: 200px;
    text-align: right;
    font-size: 17px; line-height: 1.45;
  }
  .person {
    position: absolute;
    left: 0; top: 232px;
    padding-left: 40px;
  }
  .person::before {
    content: ""; position: absolute;
    left: 0; top: 6px;
    width: 14px; height: 46px;
    background: var(--ink);
  }
  .person__name {
    font-size: 26px; font-weight: 700;
    text-transform: uppercase; letter-spacing: 0.5px;
  }
  .person__title { font-size: 15px; }
  .contacts {
    position: absolute;
    left: 40px; top: 310px;
    width: 300px;
    border-top: 1px solid var(--rule);
    padding-top: 12px;
    list-style: none;
    font-size: 16px; line-height: 1.45;
  }
  .contacts li { display: flex; align-items: center; gap: 10px; }
  .contacts svg { width: 12px; height: 12px; flex: none; }
</style>
</head>
<body>

<section class="card card--back" aria-label="Card back">
  <div class="brand"><span class="brand__dot"></span>Brenner's Detail Shop</div>
  <p class="slogan">We take pride in your ride</p>
  <p class="services">Cars – Trucks – Motorcycles and RVs</p>
</section>

<section class="card card--front" aria-label="Card front">
  <div class="brand"><span class="brand__dot"></span>Brenner's Detail Shop</div>
  <div class="front__rule"></div>
  <address class="address" style="font-style:normal">7384 E Harlow Ave<br>Spokane WA 99342</address>
  <div class="person">
    <p class="person__name">Dorian Vale</p>
    <p class="person__title">Director</p>
  </div>
  <ul class="contacts">
    <li>
      <svg viewBox="0 0 12 12" aria-hidden="true"><path d="M2 1h2.5l1 3-1.5 1a6 6 0 0 0 3 3l1-1.5 3 1V10a1 1 0 0 1-1 1A9 9 0 0 1 1 2a1 1 0 0 1 1-1z" fill="#000"/></svg>
      482.615.7734
    </li>
    <li>
      <svg viewBox="0 0 12 12" aria-hidden="true"><rect x="0.5" y="2" width="11" height="8" fill="none" stroke="#000"/><path d="M0.5 2 6 6.5 11.5 2" fill="none" stroke="#000"/></svg>
      BrennersDetail@quorvail.com
    </li>
    <li>
      <svg viewBox="0 0 12 12" aria-hidden="true"><circle cx="6" cy="6" r="5.3" fill="none" stroke="#000"/><ellipse cx="6" cy="6" rx="2.3" ry="5.3" fill="none" stroke="#000"/><path d="M0.7 6h10.6" stroke="#000"/></svg>
      www.BrennersDetail.com
    </li>
  </ul>
</section>

</body>
</html>
```